Moravine Studio Website Re-Design

I am an interior designer. What I do, is work with customers to design spaces in their homes prior to a contractor doing the work. This could be kitchens, bathrooms, offices, and more. I have uploaded a file, and it has my URL within it for you to use as a reference.
https://moravinestudio.example/

Industry/Entity Type

Interior Design

Coding

Coded - Design and coding required

Number of Pages Required

5+ page

Requirements
Must have
• Clean, professional, easy to navigate, color schemes should follow what is on my current site, also written content you can pull from my current site as well along with the current script / font

```html
<!DOCTYPE html>
<html lang="en">
<head>
<meta charset="utf-8">
<title>Moravine Studio</title>
<link href="https://fonts.googleapis.com/css2?family=Playfair+Display:wght@400;500;700&family=Montserrat:wght@400;500;600;700&display=swap" rel="stylesheet">
<style>
:root{
  --gold:#D9A21E;
  --ink:#141414;
  --black:#0b0b0b;
  --paper:#F7F6F4;
  --text:#2b2b2b;
  --white:#ffffff;
}
*{margin:0;padding:0;box-sizing:border-box}
html,body{width:1200px;height:3495px;overflow:hidden}
body{background:var(--paper);font-family:"Montserrat",sans-serif;color:var(--text);position:relative}
.abs{position:absolute}
.serif{font-family:"Playfair Display",serif}
.btn{position:absolute;background:var(--gold);color:#3a2a05;border-radius:22px;display:flex;align-items:center;justify-content:center;font-size:16px}

/* header */
.site-header{position:absolute;left:0;top:0;width:1200px;height:113px;background:var(--white);z-index:3}
.brand{position:absolute;left:112px;top:38px;font-family:"Playfair Display",serif;font-size:30px;color:var(--ink);letter-spacing:.5px}
.main-nav a{position:absolute;top:47px;font-size:14px;color:var(--text);text-decoration:none}

/* hero */
.hero{position:absolute;left:0;top:113px;width:1200px;height:622px;border-radius:0 0 170px 170px;border-bottom:7px solid var(--gold);border-left:3px solid var(--gold);border-right:3px solid var(--gold);overflow:hidden;z-index:2;
  background:linear-gradient(180deg,#f4f5f6 0%,#e2e4e6 45%,#b9bbbd 70%,#8f8f8f 100%)}
.hero-photo{position:absolute;inset:0;background:linear-gradient(160deg,rgba(255,255,255,.7) 0%,rgba(255,255,255,0) 45%),linear-gradient(0deg,rgba(150,100,70,.35) 0%,rgba(0,0,0,0) 40%)}
.hero-title{position:absolute;left:0;width:1194px;top:210px;text-align:center;font-family:"Playfair Display",serif;font-weight:700;font-size:66px;color:var(--ink);letter-spacing:-1px}

/* services band */
.services{position:absolute;left:0;top:600px;width:1200px;height:680px;background:var(--black);border-radius:0 0 170px 170px;border-bottom:7px solid var(--gold);border-left:3px solid var(--gold);border-right:3px solid var(--gold);z-index:1}
.service-card{position:absolute;top:258px;width:315px}
.service-photo{width:315px;height:227px}
.service-arrow{position:absolute;top:199px;right:6px;width:72px;height:72px;border-radius:50%;background:var(--gold);display:flex;align-items:center;justify-content:center}
.service-title{margin-top:14px;font-family:"Playfair Display",serif;font-weight:500;font-size:22px;line-height:31px;color:var(--white);width:210px;letter-spacing:-.4px}

/* features */
.feature{position:absolute;left:600px;width:490px}
.feature h3{font-family:"Playfair Display",serif;font-weight:500;font-size:22px;color:var(--ink);letter-spacing:-.4px;margin-bottom:4px}
.feature p{font-size:16px;line-height:29px;color:var(--text)}
.gold-line{position:absolute;background:var(--gold)}

/* founder */
.founder-name{position:absolute;left:111px;top:2155px;font-family:"Playfair Display",serif;font-size:31px;color:var(--ink);letter-spacing:-.5px}
.founder-role{position:absolute;left:111px;top:2230px;font-size:16px}
.founder-bio{position:absolute;left:111px;top:2278px;width:478px;font-size:16px;line-height:31px;text-align:justify}

/* rooms */
.room{position:absolute;top:2677px;width:200px;text-align:center}
.room-circle{width:158px;height:158px;border-radius:50%;background:var(--gold);margin:0 auto}
.room-label{margin-top:20px;font-weight:700;font-size:21px;color:var(--ink)}

/* footer */
.site-footer{position:absolute;left:0;top:3020px;width:1200px;height:475px;border-top:7px solid var(--gold);border-left:3px solid var(--gold);border-right:3px solid var(--gold);border-radius:230px 230px 0 0;border-bottom:none}
.footer-brand{position:absolute;left:0;width:1194px;top:80px;text-align:center;font-family:"Playfair Display",serif;font-size:40px;color:var(--ink);letter-spacing:.5px}
.footer-info{position:absolute;font-size:16px;line-height:29px;color:var(--ink)}
.footer-info .phone{font-weight:700;font-size:18px}
.social{position:absolute;top:3312px;width:32px;height:32px;border-radius:50%;background:var(--gold)}
.footer-rule{position:absolute;left:111px;top:3403px;width:978px;height:2px;background:var(--gold)}
.copyright{position:absolute;left:0;width:1200px;top:3434px;text-align:center;font-size:14px;color:var(--text)}
</style>
</head>
<body>

<header class="site-header">
  <div class="brand">Moravine Studio</div>
  <nav class="main-nav">
    <a style="left:420px">About</a>
    <a style="left:506px">Portfolio</a>
    <a style="left:608px">Our Services</a>
    <a style="left:737px">FAQs</a>
    <a style="left:816px">Contact</a>
  </nav>
  <div class="btn" style="left:973px;top:36px;width:141px;height:42px;font-size:17px">Call Now</div>
</header>

<section class="hero">
  <div class="hero-photo" role="img" aria-label="Bright modern office with white desks, black chairs and city windows"></div>
  <h1 class="hero-title">MORAVINE STUDIO</h1>
  <div class="btn" style="left:526px;top:192px;width:142px;height:42px">Get Started</div>
</section>

<section class="services">
  <div class="service-card" style="left:112px">
    <div class="service-photo" role="img" aria-label="Designer sketching a floor plan with a colour swatch fan" style="background:linear-gradient(135deg,#c4653a 0%,#e9e3dc 45%,#f4f2ef 100%)"></div>
    <div class="service-arrow"><svg width="28" height="20" viewBox="0 0 28 20"><path d="M2 10H25M17 2l8 8-8 8" fill="none" stroke="#141414" stroke-width="2.5" stroke-linecap="round" stroke-linejoin="round"/></svg></div>
    <div class="service-title">Residential Design</div>
  </div>
  <div class="service-card" style="left:442px">
    <div class="service-photo" role="img" aria-label="Bathroom renovation half rendered, half sketched" style="background:linear-gradient(90deg,#d8cbb6 0%,#ece6dc 55%,#f7f7f7 100%)"></div>
    <div class="service-arrow"><svg width="28" height="20" viewBox="0 0 28 20"><path d="M2 10H25M17 2l8 8-8 8" fill="none" stroke="#141414" stroke-width="2.5" stroke-linecap="round" stroke-linejoin="round"/></svg></div>
    <div class="service-title">Home Renovations &amp; Remodels</div>
  </div>
  <div class="service-card" style="left:771px">
    <div class="service-photo" role="img" aria-label="Material samples with a brass handle and wood swatches" style="background:linear-gradient(135deg,#2a2a2a 0%,#8a7d6c 45%,#cfc6b8 75%,#3a3a3a 100%)"></div>
    <div class="service-arrow"><svg width="28" height="20" viewBox="0 0 28 20"><path d="M2 10H25M17 2l8 8-8 8" fill="none" stroke="#141414" stroke-width="2.5" stroke-linecap="round" stroke-linejoin="round"/></svg></div>
    <div class="service-title">Furnish &amp; Style</div>
  </div>
</section>

<svg class="abs" style="left:100px;top:1383px" width="466" height="527" viewBox="0 0 466 527" role="img" aria-label="Room before and after remodel, finished on the left, under construction on the right">
  <defs>
    <linearGradient id="remodelTone" x1="0" y1="0" x2="1" y2="0">
      <stop offset="0" stop-color="#d89a6a"/><stop offset=".48" stop-color="#e8cba8"/>
      <stop offset=".52" stop-color="#e7e3de"/><stop offset="1" stop-color="#c9c3ba"/>
    </linearGradient>
  </defs>
  <polygon points="0,92 335,0 466,100 466,140 335,30 0,118" fill="#D9A21E"/>
  <polygon points="0,112 335,22 466,128 466,527 0,527" fill="url(#remodelTone)"/>
</svg>

<div class="feature" style="top:1498px">
  <h3>Innovative Home Remodeling</h3>
  <p>Full-Service Residential Remodel Company. Project Management. 2D &amp; 3D Renderings and Interior Design.</p>
</div>
<div class="feature" style="top:1615px">
  <h3>Exceptional Service</h3>
  <p>Experience Dedication in Every Detail. Our team of interior designers and contractors are committed to delivering a successful project.</p>
</div>
<div class="feature" style="top:1760px">
  <h3>The Modern Approach</h3>
  <p>Our goal is to illustrate the ways in which great design can improve the quality of your life! We consider the elements of flow, function, and aesthetic components of the remodel.</p>
</div>

<div class="gold-line" style="left:384px;top:1910px;width:2px;height:45px"></div>
<div class="gold-line" style="left:384px;top:1953px;width:772px;height:2px"></div>
<div class="gold-line" style="left:1154px;top:1953px;width:2px;height:313px"></div>
<div class="gold-line" style="left:1103px;top:2264px;width:53px;height:2px"></div>

<div class="founder-name">Clara Venn</div>
<div class="founder-role">Principle Lead Designer and Moravine Studio Founder</div>
<p class="founder-bio">Clara is known for her passion in creating elegant and inviting spaces. She delivers creative elements, inspiration, and quality designs to a broad range of residential interiors, luxury apartments, and vacation homes. She strives to keep interiors comfortable &amp; functional while introducing the classic trends in design.</p>

<svg class="abs" style="left:637px;top:2015px" width="466" height="525" viewBox="0 0 466 525" role="img" aria-label="Portrait of the founder standing in her home office">
  <defs>
    <linearGradient id="officeTone" x1="0" y1="0" x2="1" y2="1">
      <stop offset="0" stop-color="#2e2b29"/><stop offset=".5" stop-color="#5a4d44"/><stop offset="1" stop-color="#1d1c1c"/>
    </linearGradient>
  </defs>
  <polygon points="0,92 335,0 466,100 466,140 335,30 0,118" fill="#D9A21E"/>
  <polygon points="0,112 335,22 466,128 466,525 0,525" fill="url(#officeTone)"/>
</svg>

<div class="room" style="left:94px"><div class="room-circle" role="img" aria-label="Kitchen icon"></div><div class="room-label">Kitchens</div></div>
<div class="room" style="left:299px"><div class="room-circle" role="img" aria-label="Bathroom icon"></div><div class="room-label">Bathrooms</div></div>
<div class="room" style="left:503px"><div class="room-circle" role="img" aria-label="Office icon"></div><div class="room-label">Offices</div></div>
<div class="room" style="left:708px"><div class="room-circle" role="img" aria-label="Living room icon"></div><div class="room-label">Living Room</div></div>
<div class="room" style="left:912px"><div class="room-circle" role="img" aria-label="Game room icon"></div><div class="room-label">Game Room</div></div>

<footer class="site-footer">
  <div class="footer-brand">Moravine Studio</div>
</footer>
<div class="btn" style="left:108px;top:3252px;width:141px;height:42px">Contact</div>

<svg class="abs" style="left:356px;top:3244px" width="12" height="16" viewBox="0 0 12 16"><path d="M6 0a6 6 0 0 0-6 6c0 4.5 6 10 6 10s6-5.5 6-10a6 6 0 0 0-6-6zm0 8.5A2.5 2.5 0 1 1 6 3.5a2.5 2.5 0 0 1 0 5z" fill="#D9A21E"/></svg>
<svg class="abs" style="left:354px;top:3306px" width="16" height="16" viewBox="0 0 24 24"><path d="M6.6 10.8a15.1 15.1 0 0 0 6.6 6.6l2.2-2.2a1 1 0 0 1 1-.25 11.4 11.4 0 0 0 3.6.57 1 1 0 0 1 1 1V20a1 1 0 0 1-1 1A17 17 0 0 1 3 4a1 1 0 0 1 1-1h3.5a1 1 0 0 1 1 1c0 1.25.2 2.46.57 3.6a1 1 0 0 1-.25 1z" fill="#D9A21E"/></svg>
<div class="footer-info" style="left:383px;top:3238px">
  Serving the Brookhollow Valley and surrounding areas<br>
  Brookhollow Valley, OR<br>
  <span class="phone">555-014-2290</span>
</div>
<div class="footer-info" style="left:904px;top:3238px">
  Mon-Fri | 9am-5pm<br>
  Sat &amp; Sun | Closed
</div>
<div class="social" style="left:903px" role="img" aria-label="Social profile link"></div>
<div class="social" style="left:950px" role="img" aria-label="Social profile link"></div>

<div class="footer-rule"></div>
<div class="copyright">© Copyrights 2023 Moravine Studio | All Rights Reserved</div>

</body>
</html>
```